Redesign start page for existing online shop

We are selling building material (chimneys and flue pipes) as well as fireplaces (stoves). For this online shop we need a new start page. The domain is brunnfeld-bauwaren.de. Here you can see the current design. We want a smoother design with just one banner in the middle instead of the three in the first row. The look has to be more professional and trustworthy. You can therefore play with the colors. We want to try some different orange instead of our yellow / orange color. A few more things: - The phone number has to be bigger and more highlighted - So the 5 advantages at the top should be shown in a different way - New design for the products below - New footer

Target Market(s)

Germany and other countries in Europe.

Industry/Entity Type

Home Builder

Number of Pages Required

1 page

Other font styles liked:
• Please se the font on our current site.

Colors
f78f20
f68d4c

Requirements
Must have
• - Clear design - Trustworthy look - All elements Which are now shown shoulderstand be still there after redesigning -
Nice to have
• - See the Following sites to have a clou about our wishes: kalvesto.de flinkrabe.de

```html
<!DOCTYPE html>
<html lang="de">
<head>
<meta charset="utf-8">
<title>Brunnfeld Bauwaren – Startseite</title>
<link rel="stylesheet" href="https://fonts.googleapis.com/css2?family=Open+Sans:wght@400;600;700;800&display=swap">
<style>
  :root {
    --black: #000000;
    --ink: #0d0d0d;
    --white: #ffffff;
    --nav: #4f6169;
    --pill: #4b5a61;
    --yellow: #f9d13f;
    --gold: #f6c933;
    --brand-red: #e0301e;
    --logo-orange: #f7a21b;
    --text-dark: #222222;
  }
  * { margin: 0; padding: 0; box-sizing: border-box; }
  html, body { width: 1200px; height: 1024px; overflow: hidden; background: var(--white); }
  body { font-family: "Open Sans", Arial, sans-serif; color: var(--text-dark); }
  .page { position: relative; width: 1200px; height: 1024px; }
  .site { position: absolute; left: 138px; top: 0; width: 923px; height: 1024px; }

  .topbar { position: absolute; left: 0; top: 0; width: 923px; height: 35px; background: var(--black); }
  .topbar-link { position: absolute; top: 8px; display: flex; align-items: center; gap: 10px; color: var(--white); font-size: 9px; }
  .topbar-link.account { left: 718px; }
  .topbar-link.cart { left: 817px; }

  .header { position: absolute; left: 0; top: 35px; width: 923px; height: 102px; background: var(--white); }
  .brand { position: absolute; left: 28px; top: 30px; display: flex; align-items: center; gap: 8px; }
  .brand-mark { width: 38px; height: 38px; border-radius: 50%; border: 3px solid var(--logo-orange); }
  .brand-name { font-size: 17px; line-height: 17px; font-weight: 600; color: #3a3a3a; }
  .search { position: absolute; left: 459px; top: 38px; width: 157px; height: 27px; border-radius: 14px; background: var(--pill); display: flex; align-items: center; padding: 0 8px 0 16px; justify-content: space-between; }
  .search-hint { font-size: 7px; color: #e6e6e6; }
  .hotline { position: absolute; left: 660px; top: 30px; display: flex; gap: 8px; align-items: flex-start; }
  .hotline-number { font-size: 22px; font-weight: 700; letter-spacing: 2.2px; color: var(--black); line-height: 24px; }
  .hotline-hours { font-size: 9px; font-weight: 700; letter-spacing: 1px; text-align: right; color: var(--black); }

  .main-nav { position: absolute; left: 0; top: 137px; width: 923px; height: 53px; background: var(--nav); }
  .main-nav a { position: absolute; top: 17px; color: var(--white); text-decoration: none; font-size: 14.5px; letter-spacing: 1.6px; }

  .hero { position: absolute; left: 0; top: 190px; width: 923px; height: 443px;
    background: radial-gradient(ellipse at 50% 30%, #8a8a8a 0%, #5c5c5c 45%, #2b2b2b 100%); }
  .hero-scene { position: absolute; inset: 0; background: linear-gradient(180deg, transparent 55%, rgba(20,20,20,.75) 100%); }
  .hero-title { position: absolute; left: 0; right: 0; top: 236px; text-align: center; color: var(--white); font-size: 54px; font-weight: 700; letter-spacing: 9px; }

  .brands { position: absolute; left: 0; top: 633px; width: 923px; height: 86px; background: var(--yellow); }
  .brands-label { position: absolute; left: 153px; top: 35px; font-size: 12.5px; font-weight: 700; color: var(--brand-red); }
  .brand-item { position: absolute; top: 33px; font-size: 17px; font-weight: 700; color: var(--brand-red); }

  .benefits { position: absolute; left: 0; top: 719px; width: 923px; height: 305px; background: var(--ink); }
  .benefit { position: absolute; top: 72px; width: 200px; text-align: center; color: var(--gold); font-size: 14px; line-height: 20px; }
  .benefit-icon { position: absolute; width: 100px; height: 90px; }
</style>
</head>
<body>
<div class="page">
  <div class="site">
    <div class="topbar">
      <div class="topbar-link account">Mein Konto
        <svg width="22" height="22" viewBox="0 0 22 22" fill="none" stroke="#fff" stroke-width="1.2"><circle cx="11" cy="11" r="10"/><circle cx="11" cy="8.5" r="3.5"/><path d="M4.5 18c1.5-3.5 3.8-5 6.5-5s5 1.5 6.5 5"/></svg>
      </div>
      <div class="topbar-link cart">Warenkorb
        <svg width="20" height="18" viewBox="0 0 20 18" fill="none" stroke="#fff" stroke-width="1.3"><path d="M1 5h18l-3 11H4z"/><path d="M6 5l4-4 4 4"/><path d="M7 9h6M7 12h6"/></svg>
      </div>
    </div>

    <header class="header">
      <div class="brand">
        <span class="brand-mark"></span>
        <span class="brand-name">BRUNNFELD<br>BAUWAREN</span>
      </div>
      <div class="search">
        <span class="search-hint">Suchbegriff oder Artikelnummer</span>
        <svg width="18" height="18" viewBox="0 0 18 18" fill="none" stroke="#fff" stroke-width="1.4"><circle cx="11" cy="7" r="5"/><path d="M7.5 10.5L2 16"/></svg>
      </div>
      <div class="hotline">
        <svg width="32" height="42" viewBox="0 0 32 42" fill="none" stroke="#111" stroke-width="1.6"><path d="M9 3l4 9-4 3c2 8 6 14 11 18l4-3 6 7-4 3C14 38 4 24 4 8z"/></svg>
        <div>
          <div class="hotline-number">08153/472 318 0</div>
          <div class="hotline-hours">MON - FRI 9:00 TO 6:00 P.M.</div>
        </div>
      </div>
    </header>

    <nav class="main-nav">
      <a style="left:28px">ONLINE SHOP</a>
      <a style="left:171px">SERVICE</a>
      <a style="left:267px">STANDORTE I</a>
      <a style="left:388px">FÜR HÄNDLER I</a>
      <a style="left:531px">INSTALLATEURE</a>
    </nav>

    <section class="hero" role="img" aria-label="Schwarzweißfoto eines Industrieschornsteins vor bewölktem Himmel">
      <div class="hero-scene"></div>
      <h1 class="hero-title">SCHORNSTEIN</h1>
    </section>

    <section class="brands">
      <span class="brands-label">Unsere Marken</span>
      <span class="brand-item" style="left:346px">Vendrik</span>
      <span class="brand-item" style="left:532px">Ostler</span>
      <span class="brand-item" style="left:681px">Haldmann + Roth</span>
    </section>

    <section class="benefits">
      <svg class="benefit-icon" style="left:198px;top:68px" viewBox="0 0 100 90" fill="none" stroke="#f6c933" stroke-width="3" stroke-linejoin="round">
        <path d="M20 75l45-45 6 6-45 45z"/>
        <path d="M62 20c5-5 12-5 16 0l-6 6 4 4 6-6c4 5 3 12-2 16l-6-2-36 36-6-6 36-36z"/>
        <path d="M78 75L40 37l5-5 38 38z"/>
        <path d="M28 12l14-4 8 8-6 6-10-2-6 6-6-6z"/>
      </svg>
      <div class="benefit" style="left:148px;top:170px">Mounting Service</div>

      <div class="benefit-icon" style="left:422px;top:68px;width:78px;height:80px;background:linear-gradient(180deg,#f6c933,#d9a91d);opacity:.9;border-radius:6px" role="img" aria-label="Emblem mit Bundesadler als Zeichen für Herstellung in Deutschland"></div>
      <div class="benefit" style="left:362px;top:171px">Made in Germany<br>with 25 years warranty</div>

      <svg class="benefit-icon" style="left:645px;top:70px" viewBox="0 0 100 90" fill="none" stroke="#f6c933" stroke-width="3" stroke-linejoin="round">
        <path d="M8 6h62v40M8 6v76h60"/>
        <path d="M18 18h30M18 30h36M18 42h28M18 54h30M18 66h24"/>
        <path d="M54 18l4 4 8-8"/>
        <path d="M50 74l38-38 8 8-38 38-10 2z"/>
      </svg>
      <div class="benefit" style="left:596px;top:172px">Free Advisement</div>
    </section>
  </div>
</div>
</body>
</html>
```